Web application design for investigative software

ThreadKove is an investigation web application that would organize, create visualizations and allow collaboration. It’s available to anyone and can be used by students, historians, watchdog groups, civic hackers, investigative reporters, mystery enthusiasts, authors, even conspiracy theorists.

We are looking for two related pages. The first, a splash, or front, page and the second a ‘template’ for the web application. They should both be styled the same. The only restriction is that the logo is set.

The design should also be modern and visually well organized — employing a combination of visual devices and info graphics. Keep it light and not too heavy but strong/ professional. Do not be influenced by the current colors of threadkove.example, though the colors should be compatible with the logo..

The pages should be compatible with bootstrap, mostly for it’s JS and component functionality. It can be advised by the designer that a subset of bootstrap be used.

The splash page.
Something along the lines of (though not a copy of) :
https://www.brimloft.example/advertise
http://www.palvornhosting.example/
http://www.murkelsoft.example/
http://www.vontasky.example/

I have a very rough wire frame ish html file uploaded. Use a a guide, but alternate ideas are encouraged.

The application page should have some sort of bar for at the top for system level links a header and a footer. A vertical column to the left between the header and footer for ads, though this will be dynamic as a user can pay out of seeing adds. All dynamic actions will be made by the developers at ThreadKove.

WARNING. Please do not submit pre-made templates from some template website. We can do that ourselves for free.

This project will deliver CODE. HTML, CSS and supporting graphics and files.

```html
<!DOCTYPE html>
<html lang="en">
<head>
<meta charset="utf-8">
<title>ThreadKove — Track, Relate, Investigate, Solve</title>
<link rel="stylesheet" href="https://fonts.googleapis.com/css2?family=Archivo+Narrow:wght@400;700&family=Oswald:wght@600;700&family=Arimo:wght@400;700&display=swap">
<style>
:root{
  --red:#c4161c;
  --red-dark:#8e0f12;
  --ink:#2b2b2b;
  --text:#555;
  --muted:#8a8a8a;
  --bar:#1c1c1c;
  --band:#efefef;
  --band-light:#f6f6f6;
  --white:#fff;
  --social:#8f8f8f;
  --like:#4267b2;
}
*{box-sizing:border-box;margin:0;padding:0}
html,body{width:933px;height:1200px;overflow:hidden;background:var(--white)}
body{position:relative;font-family:"Arimo",Arial,sans-serif;color:var(--text)}
a{text-decoration:none;color:inherit}

/* system bar */
.system-bar{position:absolute;left:0;top:0;width:933px;height:30px;background:var(--bar)}
.system-links{position:absolute;left:612px;top:0;display:flex;height:30px}
.system-links a{display:flex;align-items:center;justify-content:center;height:30px;border:1px solid var(--red-dark);color:var(--red);font:700 8px "Arimo",Arial,sans-serif;margin-right:3px}
.system-links .search{width:32px}
.system-links .login{width:50px}
.system-links .register{width:52px}
.system-links .about{width:45px;margin-right:0}

/* header */
.site-header{position:absolute;left:0;top:30px;width:933px;height:63px;background:linear-gradient(#fafafa,#e9e9e9)}
.brand{position:absolute;left:135px;top:6px;display:flex;align-items:center;gap:7px}
.brand-dot{width:44px;height:44px;border-radius:50%;background:var(--red)}
.brand-name{font:700 23px/1 "Arimo",Arial,sans-serif;color:var(--red)}
.brand-tag{font:400 7px "Arimo",Arial,sans-serif;color:var(--ink);margin-top:3px}
.main-nav{position:absolute;left:692px;top:27px;display:flex;align-items:center;font-size:10px}
.main-nav .active{color:var(--red);font-weight:700}
.main-nav .sep{width:1px;height:14px;background:#ccc;margin:0 14px}
.main-nav .link{color:#aaa}

/* hero */
.hero{position:absolute;left:0;top:93px;width:933px;height:307px;background:radial-gradient(ellipse at 70% 40%,#e5654a 0%,#b2301e 40%,#5a1410 75%,#2a0a08 100%)}
.hero-title{position:absolute;left:152px;top:150px;font:700 60px/1 "Oswald",Impact,sans-serif;color:var(--white);letter-spacing:-1px}
.hero-accent{position:absolute;left:340px;top:204px;width:146px;height:5px;background:var(--red)}
.hero-lead{position:absolute;left:142px;top:207px;width:358px;height:51px;background:var(--white);font:400 12px/15px "Arimo",Arial,sans-serif;color:var(--ink);padding:10px 12px 0 18px;text-align:center;box-shadow:0 2px 4px rgba(0,0,0,.3)}
.hero-btn{position:absolute;top:270px;width:179px;height:28px;background:var(--white);display:flex;align-items:center;justify-content:center;gap:6px;font:400 10px "Arimo",Arial,sans-serif;color:var(--ink);border-bottom:2px solid #bbb}
.hero-btn.primary{left:141px;color:var(--red);font-weight:700;border:2px solid var(--red)}
.hero-btn.secondary{left:323px}

/* welcome */
.welcome{position:absolute;left:133px;top:358px;width:667px;height:192px;background:var(--white);box-shadow:0 0 6px rgba(0,0,0,.2);padding:24px 12px 0;text-align:center}
.welcome h1{font:700 21px/1 "Archivo Narrow","Arial Narrow",sans-serif;color:var(--red);padding-bottom:7px;border-bottom:1px solid #ddd;margin-bottom:8px}
.welcome p{font-size:8px;line-height:10px;color:var(--muted);margin-bottom:9px}

/* features */
.feature-band{position:absolute;left:0;top:551px;width:933px;height:139px;background:var(--band)}
.tile{position:absolute;top:6px;width:220px;height:127px;overflow:hidden}
.tile.organize{left:133px;background:linear-gradient(135deg,#3a3a3a,#8a8a8a 60%,#4a4a4a)}
.tile.visualize{left:357px;width:219px;background:linear-gradient(135deg,#6a1410,#b83a2a 55%,#7a1a14)}
.tile.collaborate{left:580px;background:linear-gradient(135deg,#c9c9c9,#9c9c9c 60%,#d6d6d6)}
.tile-label{position:absolute;right:12px;bottom:10px;font:700 18px/1 "Archivo Narrow","Arial Narrow",sans-serif;color:var(--white);text-decoration:underline}
.tile-rule{position:absolute;left:0;bottom:16px;width:140px;height:1px;background:rgba(255,255,255,.8)}
.tile.visualize .tile-label{bottom:auto;top:54px}
.tile.visualize .tile-rule{bottom:auto;top:71px}
.tile-copy{position:absolute;left:44px;top:78px;width:168px;text-align:right;font:400 10px/11px "Arimo",Arial,sans-serif;color:var(--white)}

/* shared */
.section-title{font:700 21px/1 "Archivo Narrow","Arial Narrow",sans-serif;color:var(--red)}
.share{position:absolute;display:flex;gap:3px;align-items:center}
.share span{height:15px;font:700 8px/15px "Arimo",Arial,sans-serif;color:var(--white);background:var(--like);padding:0 5px;border-radius:2px}
.share .count{background:var(--white);color:var(--ink);border:1px solid #bbb;font-weight:400;line-height:13px;padding:0 3px}
.art{position:absolute}

/* how it works */
.how{position:absolute;left:0;top:690px;width:933px;height:182px;background:var(--white)}
.how .section-title{position:absolute;left:133px;top:33px}
.how .share{left:504px;top:37px}
.how .rule{position:absolute;left:133px;top:56px;width:463px;height:1px;background:#ddd}
.how p{position:absolute;left:133px;top:68px;width:460px;font-size:10.4px;line-height:12.6px;color:var(--ink)}
.how .art{left:622px;top:15px;width:165px;height:146px;border-radius:22px;background:radial-gradient(circle at 50% 50%,#d8cdb6,#8e8574 60%,transparent 72%)}

/* what you get */
.offer{position:absolute;left:0;top:872px;width:933px;height:165px;background:var(--band-light)}
.offer .art{left:158px;top:10px;width:140px;height:146px;background:radial-gradient(circle at 50% 50%,#7fb6d9,#b45ab0 40%,#cfcfcf 62%,transparent 72%)}
.offer .share{left:338px;top:33px}
.offer .section-title{position:absolute;right:133px;top:30px}
.offer .rule{position:absolute;left:338px;top:56px;width:462px;height:1px;background:#ddd}
.offer p{position:absolute;left:338px;width:462px;text-align:center;font-size:9.6px;line-height:11px;color:var(--muted)}
.offer .p1{top:65px}
.offer .p2{top:115px}

/* footer */
.site-footer{position:absolute;left:0;top:1037px;width:933px;height:133px;background:var(--white)}
.footer-col{position:absolute;top:23px}
.footer-col h2{font:700 11px/1 "Archivo Narrow","Arial Narrow",sans-serif;color:var(--ink);margin-bottom:10px}
.products{left:133px;width:170px;font-size:8.6px;line-height:10px;color:var(--ink)}
.products b{font-weight:700}
.products .hl{color:var(--red);font-weight:700}
.social{left:358px}
.social-icons{display:flex;gap:4px}
.social-icons span{width:28px;height:28px;background:var(--social)}
.social-icons span.alt{background:#2d4f8f}
.social-icons span.mid{background:#555}
.footer-brand{position:absolute;left:612px;top:41px}
.footer-brand .brand{position:static;gap:4px}
.footer-brand .brand-dot{width:22px;height:22px}
.footer-brand .brand-name{font-size:12px}
.footer-brand .brand-tag{font-size:4px;margin-top:1px}
.copyright{font-size:7px;color:var(--ink);margin-top:8px}

/* legal bar */
.legal-bar{position:absolute;left:0;top:1170px;width:933px;height:30px;background:var(--bar);display:flex;justify-content:center;align-items:center}
.legal-bar a{font:700 7px "Arimo",Arial,sans-serif;color:var(--white);padding:0 10px;border-left:1px solid #888;line-height:10px}
.legal-bar a:first-child{border-left:0}
</style>
</head>
<body>

<nav class="system-bar" aria-label="System">
  <div class="system-links">
    <a class="search" href="#" aria-label="Search">
      <svg width="10" height="10" viewBox="0 0 10 10"><circle cx="4" cy="4" r="3" fill="none" stroke="#c4161c" stroke-width="1.3"/><line x1="6.2" y1="6.2" x2="9.2" y2="9.2" stroke="#c4161c" stroke-width="1.3"/></svg>
    </a>
    <a class="login" href="#">Login</a>
    <a class="register" href="#">Register</a>
    <a class="about" href="#">About</a>
  </div>
</nav>

<header class="site-header">
  <a class="brand" href="#">
    <span class="brand-dot"></span>
    <span>
      <span class="brand-name">ThreadKove</span>
      <span class="brand-tag" style="display:block">Track, Relate, Investigate, Solve!</span>
    </span>
  </a>
  <nav class="main-nav">
    <a class="active" href="#">Home</a>
    <span class="sep"></span>
    <a class="link" href="#">Application</a>
  </nav>
</header>

<section class="hero" role="img" aria-label="Photo of a hand touching a tablet surrounded by sketched icons of mail, phones, locks, calendars and map pins in warm red tones">
</section>
<div class="hero-title">THREADKOVE</div>
<div class="hero-accent"></div>
<p class="hero-lead">is an on-line system that allows you to enter what you know about a person, event, object, or group.</p>
<a class="hero-btn primary" href="#">Start Application
  <svg width="11" height="11" viewBox="0 0 11 11"><circle cx="5.5" cy="5.5" r="4.6" fill="none" stroke="#c4161c" stroke-width="1.2"/><path d="M3 5.5h5M6 3.5l2 2-2 2" fill="none" stroke="#c4161c" stroke-width="1.2"/></svg>
</a>
<a class="hero-btn secondary" href="#">Register Now!
  <svg width="11" height="11" viewBox="0 0 11 11"><circle cx="5.5" cy="5.5" r="4.6" fill="none" stroke="#2b2b2b" stroke-width="1.2"/><path d="M3 5.5h5M6 3.5l2 2-2 2" fill="none" stroke="#2b2b2b" stroke-width="1.2"/></svg>
</a>

<section class="welcome">
  <h1>WELCOME</h1>
  <p>Have you ever compiled a lot of data about something, but been unable to figure out what it means? Often, the number of people involved, the number of events at which they might have met, and the number of common contacts are just too much for a person to track. This can happen when you are trying to understand the players and interests in current events, or the characters and actions in a novel. It's easy to collect the data, but hard to visualize it or analyze the relationships.</p>
  <p>This is where ThreadKove comes in. ThreadKove allows you to easily visualize people, events, things, groups, and timelines and to easily see the relationships between them.</p>
  <p>Use ThreadKove to plot a novel, or to investigate a crime. Use it to analyze your favorite conspiracy theory and look for relationships that have eluded the investigators. Use it to track the causes and results of historical events – or current ones. Use it to track changing relationships among your friends at high school. Use it to track the twists and turns of a role-playing game. There's no end to what you can investigate with ThreadKove</p>
</section>

<section class="feature-band">
  <div class="tile organize" role="img" aria-label="Grey photo of a hand over floating charts and dashboards">
    <span class="tile-rule"></span><span class="tile-label">Organize</span>
  </div>
  <div class="tile visualize" role="img" aria-label="Red photo of a smartphone with glowing digital symbols rising from it">
    <span class="tile-rule"></span><span class="tile-label">Visualize</span>
    <p class="tile-copy">Once data has been entered, use ThreadKove's graphical analysis tools to analyze your data in new ways.</p>
  </div>
  <div class="tile collaborate" role="img" aria-label="Photo of a businessman pointing up at a rising chart arrow drawn on a wall">
    <span class="tile-rule"></span><span class="tile-label">Colaborate</span>
  </div>
</section>

<section class="how">
  <h2 class="section-title">How does ThreadKove work?</h2>
  <div class="share"><span>Like</span><span>Share</span><span class="count">60k</span></div>
  <div class="rule"></div>
  <p>Once data has been entered, use ThreadKove's graphical analysis tools to analyze your data in new ways. Use relationship maps to find out how two people or groups are associated. Use timeline analysis to show cause and effect of seemingly unrelated events. Use social network mapping to show how relationships change over time. Look for events that stand out or relationships that have great impact on multiple events. Like a spider's web, look for the intersections that matter, then look for the players that brought that intersection into focus.</p>
  <div class="art" role="img" aria-label="Illustration of a silver smartphone surrounded by floating app icon tiles"></div>
</section>

<section class="offer">
  <div class="art" role="img" aria-label="Illustration of a cube built from colourful app icon blocks"></div>
  <div class="share"><span>Like</span><span>Share</span><span class="count">60k</span></div>
  <h2 class="section-title">What do I get with ThreadKove?</h2>
  <div class="rule"></div>
  <p class="p1">Basic ThreadKove will allow any registered user to create, maintain and analyze one investigation. Advanced features will be available a la carte and will include special analytical reports, multiple investigations, and the ability to share an investigation among multiple users. Investigations of general interest could also be shared publicly in read-only mode.</p>
  <p class="p2">You will also get access to several read-only public investigations to use as a model. These might include the plots of popular novels or movies, the details of a major political event, or an investigation into a famous crime.</p>
</section>

<footer class="site-footer">
  <div class="footer-col products">
    <h2>ALL PRODUCTS</h2>
    <span class="hl">Lorem ipsum dolor</span> - Sit amet, Consectetuer adipiscing elit - <b>sed diam</b> - Nonummy nibh - <b>Euismod tincidunt</b> - ut laoreet dolore magna - <b>aliquam erat volutpat.</b>
  </div>
  <div class="footer-col social">
    <h2>SOCIAL MEDIA</h2>
    <div class="social-icons"><span></span><span class="alt"></span><span class="mid"></span><span class="mid"></span></div>
  </div>
  <div class="footer-brand">
    <a class="brand" href="#">
      <span class="brand-dot"></span>
      <span>
        <span class="brand-name">ThreadKove</span>
        <span class="brand-tag" style="display:block">Track, Relate, Investigate, Solve!</span>
      </span>
    </a>
    <p class="copyright">© 2000-2014 ThreadKove. All rights reserved</p>
  </div>
</footer>

<nav class="legal-bar" aria-label="Legal">
  <a href="#">Privacy Policy</a>
  <a href="#">Terms of Use</a>
  <a href="#">Site map</a>
</nav>

</body>
</html>
```